Resposive web site in 4 languages + image gallery + logo design

We need a web page, which will work on all devices.
I have uploaded web page concept.
Company name: Quarnela
Industry/Entity Type
It Company
Logo Text
quality matters
Coding
Coded - Design and coding required
Number of Pages Required
1 page

```html
<!DOCTYPE html>
<html lang="en">
<head>
<meta charset="utf-8">
<title>Quarnela — Wood Works, Stone Works, Restoration</title>
<link rel="stylesheet" href="https://fonts.googleapis.com/css2?family=Raleway:wght@400;500;600;700&display=swap">
<style>
:root{
  --orange:#f39a1f;
  --orange-dark:#e0860f;
  --brand:#b8661f;
  --ink:#333333;
  --muted:#555555;
  --grey-btn:#5e5e5e;
  --wood-1:#4a2d1c;
  --wood-2:#6b4430;
  --white:#ffffff;
  --line:#d8d8d8;
  --map:#eceeef;
}
*{box-sizing:border-box;margin:0;padding:0}
html,body{width:1200px;height:2844px;overflow:hidden;background:var(--white)}
body{font-family:"Raleway",Arial,sans-serif;color:var(--ink);position:relative}
.abs{position:absolute}

/* header */
.top-rule{left:0;top:0;width:1200px;height:5px;background:var(--orange)}
.header{left:0;top:5px;width:1200px;height:84px;background:var(--white)}
.logo-tab{left:95px;top:0;width:124px;height:124px;border-radius:50%;background:var(--white);z-index:3}
.logo-dot{left:128px;top:32px;width:58px;height:58px;border-radius:50%;background:var(--brand);z-index:4}
.logo-name{left:206px;top:42px;font-size:26px;font-weight:700;color:var(--brand);z-index:4}
.nav{top:38px;font-size:16px;font-weight:500;color:#222;letter-spacing:.3px}
.nav.active{color:var(--orange)}
.nav.active::after{content:"";display:block;margin-top:8px;height:2px;background:var(--orange)}
.lang{left:823px;top:30px;width:98px;height:34px;border:1px solid #999;border-radius:3px;font-size:14px;padding:8px 0 0 14px;color:#333}
.social{width:38px;height:38px;border:1.5px solid #333;border-radius:50%}

/* hero */
.hero{left:0;top:89px;width:1200px;height:456px;background:linear-gradient(110deg,#5a3a26 0%,#8b6547 35%,#b8916c 60%,#6a4630 100%)}
.hero-box{left:100px;top:213px;width:475px;height:202px;background:rgba(40,28,20,.72);padding:18px 20px}
.hero-title{font-size:36px;font-weight:700;color:var(--orange)}
.hero-rule{width:145px;height:2px;background:var(--white);margin:10px 0 22px}
.hero-text{font-size:15px;line-height:29px;color:var(--white)}
.dot{top:507px;width:16px;height:16px;border:2px solid var(--white);border-radius:50%}
.dot.on{background:var(--orange)}

/* estimate band */
.estimate{left:0;top:545px;width:1200px;height:75px;background:var(--orange)}
.estimate-badge{left:99px;top:527px;width:112px;height:112px;border-radius:50%;background:var(--orange);border:5px solid var(--white);box-shadow:0 2px 6px rgba(0,0,0,.25)}
.estimate-text{left:252px;top:567px;font-size:21px;font-weight:600;color:var(--white)}
.btn{background:var(--grey-btn);color:var(--white);font-size:15px;display:flex;align-items:center;justify-content:center;border-radius:2px}
.quote-btn{left:840px;top:562px;width:156px;height:41px;font-size:17px}

/* section headings */
.heading{left:0;width:1200px;display:flex;justify-content:center;align-items:center;gap:12px;font-size:30px;font-weight:700;color:#333}
.heading .accent{color:var(--orange)}
.heading-dot{width:42px;height:42px;border-radius:50%;background:var(--brand)}
.intro{left:0;width:1200px;text-align:center;font-size:14px;line-height:23px;color:#333}

/* service blocks */
.photo{border:5px solid var(--white);box-shadow:0 4px 12px rgba(0,0,0,.3);overflow:hidden}
.photo-fill{width:100%;height:100%}
.photo-band{position:absolute;left:0;bottom:0;width:100%;height:62px;background:rgba(243,154,31,.85)}
.arrow{position:absolute;bottom:16px;width:30px;height:30px;border:1.5px solid var(--white);border-radius:50%}
.svc-title{font-size:20px;font-weight:700;color:var(--orange)}
.svc-rule{width:140px;height:2px;background:var(--orange);margin:10px 0 14px}
.svc-text{font-size:13px;line-height:22px;color:#333;width:600px}
.read-btn{width:108px;height:36px;font-size:14px}

/* wood bands */
.band{left:0;width:1200px;height:101px;background:linear-gradient(180deg,var(--wood-2),var(--wood-1) 50%,var(--wood-2))}
.cat{top:0;height:101px;display:flex;align-items:center;gap:12px;font-size:19px;color:var(--white)}
.cat-icon{width:52px;height:52px;border:2px solid var(--white);border-radius:50%;display:flex;align-items:center;justify-content:center}
.cat-icon.on{background:var(--orange);border-color:var(--white)}

/* about */
.about-text{left:488px;top:2158px;width:615px;font-size:13px;line-height:23px;color:#333}
.sign{font-size:15px;margin-top:30px;line-height:28px}
.sign .name{color:var(--orange);font-weight:600}

/* contact */
.contact{left:0;top:2410px;width:1200px;height:375px;background:linear-gradient(135deg,#eef0f1,#e4e7e9 60%,#eef0f1);border-top:3px solid var(--orange)}
.contact-head{left:100px;top:2450px;display:flex;align-items:center;gap:10px;font-size:29px;font-weight:700;color:#333}
.contact-head .accent{color:var(--orange)}
.c-icon{width:46px;height:46px;border-radius:50%;border:2px solid #555;background:var(--white);display:flex;align-items:center;justify-content:center}
.c-icon.on{background:var(--orange);border-color:var(--orange)}
.c-text{font-size:15px;line-height:22px;color:#333}
.form-title{left:484px;top:2454px;font-size:19px;font-weight:600;color:#222}
.field{border:1px solid #bbb;background:rgba(255,255,255,.6);font-size:14px;color:#777;padding:11px 8px}
.send{left:484px;top:2712px;width:118px;height:38px;background:var(--orange);color:var(--white);font-size:15px;display:flex;align-items:center;justify-content:center;border-radius:2px}

/* footer */
.footer{left:0;top:2785px;width:1200px;height:59px;background:linear-gradient(180deg,var(--orange),var(--orange-dark))}
.copy{left:100px;top:2805px;font-size:14px;color:var(--white)}
.f-social{top:2797px;width:34px;height:34px;border:1.5px solid var(--white);border-radius:50%}
</style>
</head>
<body>

<!-- header -->
<div class="abs top-rule"></div>
<div class="abs header"></div>
<div class="abs logo-tab"></div>
<div class="abs logo-dot"></div>
<div class="abs logo-name">Quarnela</div>
<div class="abs nav active" style="left:452px">SERVICES</div>
<div class="abs nav" style="left:564px">ABOUT US</div>
<div class="abs nav" style="left:684px">CONTACT US</div>
<div class="abs lang">ENG ▾</div>
<div class="abs social" style="left:958px;top:28px"></div>
<div class="abs social" style="left:1009px;top:28px"></div>
<div class="abs social" style="left:1060px;top:28px"></div>

<!-- hero -->
<div class="abs hero" role="img" aria-label="Craftsman planing a wooden chair frame in a carpentry workshop"></div>
<div class="abs hero-box">
  <div class="hero-title">Wood Works</div>
  <div class="hero-rule"></div>
  <p class="hero-text">Quarnela is a company whose business operations include making wooden products, restoration and building structures from natural stone.</p>
</div>
<div class="abs dot" style="left:1065px"></div>
<div class="abs dot on" style="left:1090px"></div>
<div class="abs dot" style="left:1115px"></div>
<div class="abs dot" style="left:1140px"></div>

<!-- estimate -->
<div class="abs estimate"></div>
<div class="abs estimate-badge">
  <svg width="102" height="102" viewBox="0 0 102 102" fill="none" stroke="#fff" stroke-width="3">
    <path d="M22 50 L51 26 L80 50"/>
    <rect x="30" y="48" width="42" height="28"/>
    <line x1="30" y1="57" x2="72" y2="57"/><line x1="30" y1="66" x2="72" y2="66"/>
    <rect x="46" y="60" width="10" height="16"/>
  </svg>
</div>
<div class="abs estimate-text">Are you interested in an estimate?</div>
<div class="abs btn quote-btn">Get a Quote</div>

<!-- services -->
<div class="abs heading" style="top:662px"><span class="heading-dot"></span><span>Our <span class="accent">Services</span></span></div>
<p class="abs intro" style="top:722px">Our goal is to offer suitable products and quality furniture with installation and<br>after-sales service to all of our clients</p>

<!-- wood works -->
<div class="abs photo" style="left:95px;top:817px;width:323px;height:213px">
  <div class="photo-fill" role="img" aria-label="Hands carving a turned wooden spindle on a workbench" style="background:linear-gradient(135deg,#3c2a20,#8a6a52 55%,#c7a27a)"></div>
  <div class="photo-band"></div>
  <div class="arrow" style="right:52px"></div><div class="arrow" style="right:14px"></div>
</div>
<div class="abs" style="left:466px;top:818px">
  <div class="svc-title">WOOD WORKS</div><div class="svc-rule"></div>
  <p class="svc-text">Timber is, in essence, a natural and warm material. Wood is also relatively durable and easy to work with, which has made it a favourite of builders throughout history. Our goal is to offer suitable products and quality furniture with installation and after-sales service to all of our clients. In order to achieve this, we're ready to help our clients in all stages of construction from design to production and maintenance.</p>
</div>
<div class="abs btn read-btn" style="left:466px;top:989px">Read More</div>

<div class="abs band" style="top:1073px">
  <div class="abs cat" style="left:98px"><span class="cat-icon on"><svg width="30" height="30" viewBox="0 0 30 30" fill="none" stroke="#fff" stroke-width="2"><rect x="5" y="11" width="20" height="9"/><line x1="7" y1="20" x2="7" y2="24"/><line x1="23" y1="20" x2="23" y2="24"/></svg></span>Furniture</div>
  <div class="abs cat" style="left:270px"><span class="cat-icon"><svg width="30" height="30" viewBox="0 0 30 30" fill="none" stroke="#fff" stroke-width="2"><rect x="7" y="6" width="16" height="18"/><line x1="15" y1="6" x2="15" y2="24"/></svg></span>Windows</div>
  <div class="abs cat" style="left:441px"><span class="cat-icon"><svg width="30" height="30" viewBox="0 0 30 30" fill="none" stroke="#fff" stroke-width="2"><rect x="8" y="5" width="14" height="20"/><line x1="8" y1="12" x2="22" y2="12"/><line x1="8" y1="18" x2="22" y2="18"/></svg></span>Doors</div>
  <div class="abs cat" style="left:584px"><span class="cat-icon"><svg width="30" height="30" viewBox="0 0 30 30" fill="none" stroke="#fff" stroke-width="2"><path d="M6 24 H12 V18 H18 V12 H24 V6"/></svg></span>Staircase</div>
  <div class="abs cat" style="left:757px"><span class="cat-icon"><svg width="30" height="30" viewBox="0 0 30 30" fill="none" stroke="#fff" stroke-width="2"><rect x="9" y="6" width="12" height="18" rx="3"/></svg></span>Wood Carving</div>
  <div class="abs cat" style="left:967px"><span class="cat-icon"><svg width="30" height="30" viewBox="0 0 30 30" fill="none" stroke="#fff" stroke-width="2"><path d="M6 22 L18 10 L22 14 L10 26 Z"/><line x1="18" y1="10" x2="23" y2="5"/></svg></span>Graining</div>
</div>

<!-- stone works -->
<div class="abs photo" style="left:95px;top:1218px;width:323px;height:213px">
  <div class="photo-fill" role="img" aria-label="Mason setting stone paving blocks with a rubber mallet" style="background:linear-gradient(135deg,#d9c9b6,#b09a86 50%,#5d4b40)"></div>
  <div class="photo-band"></div>
  <div class="arrow" style="right:52px"></div><div class="arrow" style="right:14px"></div>
</div>
<div class="abs" style="left:466px;top:1222px">
  <div class="svc-title">STONE WORKS</div><div class="svc-rule"></div>
  <p class="svc-text">The natural stone found in the ground has been used in construction for centuries because of its durability. A structure built by a skilled craftsman from natural stone is unique, genuine and durable, and perfect for our bracing climate.<br>Our experienced craftsmen are ready to help you in all stages of construction from planning to completion.</p>
</div>
<div class="abs btn read-btn" style="left:466px;top:1393px">Read More</div>

<div class="abs band" style="top:1477px">
  <div class="abs cat" style="left:98px"><span class="cat-icon on"><svg width="30" height="30" viewBox="0 0 30 30" fill="none" stroke="#fff" stroke-width="2"><rect x="6" y="7" width="18" height="16"/><line x1="6" y1="12" x2="24" y2="12"/><line x1="6" y1="18" x2="24" y2="18"/><line x1="15" y1="7" x2="15" y2="12"/><line x1="11" y1="12" x2="11" y2="18"/><line x1="19" y1="12" x2="19" y2="18"/></svg></span>Walls</div>
  <div class="abs cat" style="left:244px"><span class="cat-icon"><svg width="30" height="30" viewBox="0 0 30 30" fill="none" stroke="#fff" stroke-width="2"><path d="M5 13 L15 6 L25 13"/><line x1="8" y1="13" x2="8" y2="24"/><line x1="22" y1="13" x2="22" y2="24"/><line x1="15" y1="13" x2="15" y2="24"/></svg></span>Terraces</div>
  <div class="abs cat" style="left:415px"><span class="cat-icon"><svg width="30" height="30" viewBox="0 0 30 30" fill="none" stroke="#fff" stroke-width="2"><path d="M7 14 H23 V22 H7 Z"/><path d="M10 14 Q15 6 20 14"/></svg></span>Kitchens</div>
  <div class="abs cat" style="left:586px"><span class="cat-icon"><svg width="30" height="30" viewBox="0 0 30 30" fill="none" stroke="#fff" stroke-width="2"><path d="M15 5 C20 11 21 15 15 20 C9 15 10 11 15 5 Z"/><line x1="7" y1="24" x2="23" y2="24"/></svg></span>Fireplaces</div>
  <div class="abs cat" style="left:784px"><span class="cat-icon"><svg width="30" height="30" viewBox="0 0 30 30" fill="none" stroke="#fff" stroke-width="2"><circle cx="12" cy="12" r="5"/><circle cx="19" cy="18" r="5"/></svg></span>Smokeries</div>
  <div class="abs cat" style="left:972px"><span class="cat-icon"><svg width="30" height="30" viewBox="0 0 30 30" fill="none" stroke="#fff" stroke-width="2"><path d="M8 24 V9 L10 6 L12 9 V24"/><path d="M14 24 V9 L16 6 L18 9 V24"/><path d="M20 24 V9 L22 6 L24 9 V24"/><line x1="6" y1="14" x2="25" y2="14"/></svg></span>Fences</div>
</div>

<!-- restoration -->
<div class="abs photo" style="left:95px;top:1622px;width:323px;height:213px">
  <div class="photo-fill" role="img" aria-label="Hands repairing the backrest of an old wooden chair" style="background:linear-gradient(135deg,#e9ddd0,#9c7458 45%,#4a2f20)"></div>
  <div class="photo-band"></div>
  <div class="arrow" style="right:52px"></div><div class="arrow" style="right:14px"></div>
</div>
<div class="abs" style="left:466px;top:1624px">
  <div class="svc-title">RESTORATION</div><div class="svc-rule"></div>
  <p class="svc-text">The natural stone found in the ground has been used in construction for centuries because of its durability. A structure built by a skilled craftsman from natural stone is unique, genuine and durable, and perfect for our bracing climate.<br>Our experienced craftsmen are ready to help you in all stages of construction from planning to completion.</p>
</div>
<div class="abs btn read-btn" style="left:466px;top:1796px">Read More</div>

<div class="abs band" style="top:1882px">
  <div class="abs cat" style="left:98px"><span class="cat-icon on"><svg width="30" height="30" viewBox="0 0 30 30" fill="none" stroke="#fff" stroke-width="2"><rect x="5" y="11" width="20" height="9"/><line x1="7" y1="20" x2="7" y2="24"/><line x1="23" y1="20" x2="23" y2="24"/></svg></span>Furniture</div>
  <div class="abs cat" style="left:270px"><span class="cat-icon"><svg width="30" height="30" viewBox="0 0 30 30" fill="none" stroke="#fff" stroke-width="2"><rect x="7" y="6" width="16" height="18"/><line x1="15" y1="6" x2="15" y2="24"/></svg></span>Windows</div>
  <div class="abs cat" style="left:441px"><span class="cat-icon"><svg width="30" height="30" viewBox="0 0 30 30" fill="none" stroke="#fff" stroke-width="2"><rect x="8" y="5" width="14" height="20"/><line x1="8" y1="12" x2="22" y2="12"/><line x1="8" y1="18" x2="22" y2="18"/></svg></span>Doors</div>
  <div class="abs cat" style="left:584px"><span class="cat-icon"><svg width="30" height="30" viewBox="0 0 30 30" fill="none" stroke="#fff" stroke-width="2"><path d="M6 24 H12 V18 H18 V12 H24 V6"/></svg></span>Staircase</div>
  <div class="abs cat" style="left:754px"><span class="cat-icon"><svg width="30" height="30" viewBox="0 0 30 30" fill="none" stroke="#fff" stroke-width="2"><path d="M4 15 L15 9 L26 15 L15 21 Z"/><path d="M4 19 L15 25 L26 19"/></svg></span>Floors</div>
  <div class="abs cat" style="left:898px"><span class="cat-icon"><svg width="30" height="30" viewBox="0 0 30 30" fill="none" stroke="#fff" stroke-width="2"><rect x="6" y="10" width="18" height="14"/><path d="M11 10 V7 H19 V10"/></svg></span>Special Projects</div>
</div>

<!-- about -->
<div class="abs heading" style="top:2014px"><span class="heading-dot"></span><span>About <span class="accent">Us</span></span></div>
<p class="abs intro" style="top:2074px">Our goal is to offer suitable products and quality furniture with installation and<br>after-sales service to all of our clients</p>
<div class="abs photo" style="left:99px;top:2155px;width:356px;height:210px">
  <div class="photo-fill" role="img" aria-label="Hard hat, rolled plans and hand tools on a wooden table" style="background:linear-gradient(135deg,#d9b93a,#8a5a34 40%,#5c3a24)"></div>
</div>
<div class="abs about-text">
  <p>Quarnela is a company whose business operations include making wooden products, restoration and building structures from natural stone. All of our products are made by craftsmen and specialists who have extensive experience and knowledge in their fields. The products we offer are always handmade and we take the requests and ideas of the specific client into account We always strive to achieve the best possible quality.</p>
  <p class="sign">Quality matters,<br><span class="name">Quarnela</span></p>
</div>

<!-- contact -->
<div class="abs contact" role="img" aria-label="Faint street map of central Tallinn behind the contact area"></div>
<div class="abs contact-head"><span class="heading-dot"></span><span>Contact <span class="accent">Us</span></span></div>

<div class="abs c-icon" style="left:98px;top:2537px"><svg width="22" height="22" viewBox="0 0 22 22" fill="none" stroke="#444" stroke-width="1.8"><rect x="2" y="5" width="18" height="12"/><path d="M2 5 L11 12 L20 5"/></svg></div>
<div class="abs c-text" style="left:167px;top:2549px">hello@quarnela.example</div>
<div class="abs c-icon on" style="left:98px;top:2612px"><svg width="22" height="22" viewBox="0 0 22 22" fill="none" stroke="#fff" stroke-width="1.8"><path d="M11 20 C5 13 5 11 5 9 A6 6 0 0 1 17 9 C17 11 17 13 11 20 Z"/><circle cx="11" cy="9" r="2"/></svg></div>
<div class="abs c-text" style="left:167px;top:2612px">Lepa 21 10111 Tallinn<br>ESTONIA</div>
<div class="abs c-icon" style="left:98px;top:2688px"><svg width="22" height="22" viewBox="0 0 22 22" fill="none" stroke="#444" stroke-width="1.8"><path d="M5 3 L9 3 L10 7 L8 9 C9 12 10 13 13 14 L15 12 L19 13 L19 17 C12 18 4 10 5 3 Z"/></svg></div>
<div class="abs c-text" style="left:167px;top:2700px">+372 55 01234</div>

<div class="abs form-title">Please Fill In The Following Fields If You Would Like A Price Quote:</div>
<div class="abs field" style="left:484px;top:2497px;width:291px;height:43px">First Name</div>
<div class="abs field" style="left:810px;top:2497px;width:290px;height:43px">Last Name</div>
<div class="abs field" style="left:484px;top:2552px;width:291px;height:43px">Phone Number</div>
<div class="abs field" style="left:810px;top:2552px;width:290px;height:43px">E-Mail Address</div>
<div class="abs field" style="left:484px;top:2607px;width:616px;height:88px">Message</div>
<div class="abs send">Send Now</div>

<!-- footer -->
<div class="abs footer"></div>
<div class="abs copy">Copyright © 2016 Quarnela - All rights reserved</div>
<div class="abs f-social" style="left:980px"></div>
<div class="abs f-social" style="left:1025px"></div>
<div class="abs f-social" style="left:1069px"></div>

</body>
</html>
```